Quorenta - Automated robotic Inspection with AI need new business cards

We need a new design of our business cards. The company is focused on automated quality control at high speed with unmatched results. We have a logo but need a more forward leaning business card that shows that we are delivering cutting edge technology.

Contact Information for Business Card

Name
Position
Adress
Phone
Email
e.g.
Lotta Berglund
Chief Financial Officer (CFO)

Quorenta Sweden AB
Rönnvägen 14, SE-175 43 JÄRFÄLLA, Sweden
Mobile: +46701 23 45 67 | Office: +46 8 52 61 74
www.quorenta-example.com

Font styles to use
Sans Serif

```html
<!DOCTYPE html>
<html lang="en">
<head>
<meta charset="utf-8">
<title>Quorenta business cards</title>
<link href="https://fonts.googleapis.com/css2?family=Roboto:wght@400;500;700&display=swap" rel="stylesheet">
<style>
  :root {
    --page: #e7e7e7;
    --card: #2d2d2e;
    --edge: #2a6fb8;
    --accent: #3a7cc4;
    --text: #d9d9d9;
    --logo-light: #ffffff;
    --logo-emboss: #4a4a4c;
    --rule: #8a8a8a;
  }
  * { margin: 0; padding: 0; box-sizing: border-box; }
  html, body { width: 1200px; height: 801px; overflow: hidden; }
  body {
    background: var(--page);
    font-family: "Roboto", Arial, sans-serif;
    position: relative;
  }
  .card {
    position: absolute;
    top: 246px;
    width: 540px;
    height: 309px;
    background: var(--card);
    border-bottom: 3px solid var(--edge);
    border-right: 2px solid var(--edge);
    box-shadow: 0 10px 24px rgba(0,0,0,0.18);
  }
  .card--front { left: 40px; }
  .card--back { left: 620px; }

  .brand {
    position: absolute;
    display: flex;
    align-items: center;
    gap: 10px;
    font-weight: 700;
    letter-spacing: 1px;
  }
  .brand__dot { border-radius: 50%; flex: none; }

  .card--front .brand {
    left: 36px;
    top: 136px;
    font-size: 34px;
    color: var(--logo-light);
  }
  .card--front .brand__dot { width: 22px; height: 22px; background: var(--logo-light); }

  .divider {
    position: absolute;
    left: 262px;
    top: 70px;
    width: 1px;
    height: 172px;
    background: var(--rule);
  }

  .contact {
    position: absolute;
    left: 284px;
    top: 70px;
    color: var(--text);
    font-size: 12px;
    line-height: 1.45;
  }
  .contact__name { color: var(--accent); font-size: 18px; font-weight: 500; line-height: 1.2; }
  .contact__role { font-size: 13.5px; margin-bottom: 14px; }
  .contact__line { display: flex; align-items: center; gap: 8px; }
  .contact__line svg { width: 11px; height: 11px; flex: none; }
  .contact__address { margin-top: 12px; }

  .card--back .brand {
    left: 0; right: 0; top: 0; bottom: 0;
    justify-content: center;
    font-size: 64px;
    color: var(--logo-emboss);
    text-shadow: none;
  }
  .card--back .brand__dot { width: 40px; height: 40px; background: var(--logo-emboss); }
</style>
</head>
<body>
  <section class="card card--front" aria-label="Business card front">
    <div class="brand"><span class="brand__dot"></span>Quorenta</div>
    <div class="divider"></div>
    <div class="contact">
      <p class="contact__name">Lotta Berglund</p>
      <p class="contact__role">Chief Financial Officer (CFO)</p>
      <p class="contact__line">
        <svg viewBox="0 0 12 12" fill="none" stroke="currentColor" stroke-width="1.4"><path d="M3 1.5 L4.5 4 L3.5 5 Q5 8 7 8.5 L8 7.5 L10.5 9 L9.5 10.5 Q4 10.5 1.5 3 Z"/></svg>
        +46 8 52 61 74
      </p>
      <p class="contact__line">
        <svg viewBox="0 0 12 12" fill="none" stroke="currentColor" stroke-width="1.4"><rect x="3" y="1" width="6" height="10" rx="1"/></svg>
        +46701 23 45 67
      </p>
      <p class="contact__line">
        <svg viewBox="0 0 12 12" fill="currentColor"><circle cx="6" cy="6" r="5"/></svg>
        www.quorenta-example.com
      </p>
      <p class="contact__address">Quorenta Sweden AB, Rönnvägen 14<br>SE-175 43 JÄRFÄLLA, Sweden</p>
    </div>
  </section>

  <section class="card card--back" aria-label="Business card back">
    <div class="brand"><span class="brand__dot"></span>Quorenta</div>
  </section>
</body>
</html>
```